Company Business Card Design Project - Revamp the image of an old construction company.

We need a business card designed for a new company in Australia.

Type of business is Commercial Roofing & Painting.

Medium will be brushed black metal card that can/will be acid etched to a brushed steel silver, acid die cut and two printed colours of our choice which will be white and pantone orange.

We have hopes that the design will be simple, modern and represent with a quick glance what our company does.

Please read instructions carefully in must have box any questions please ask.

If you are interested in this job please look at other job that we have which is very similar with logo and design

Please have a look at the things that can be done with metals cards on google images for inspiration.

Target Market(s)

Business owners, commercial property development Men from 25-70 years of age.

Industry/Entity Type

Construction

Requirements
Must have
• Front of card:

Must use the company logo and name provided as attachment (see below norwick vale construction_black_background).

the words -Commercial Painting and Roofing- must be on front of card

details needed on front or back depending on your design

Name
position
email
mobile

all details can be on front with a cool design to be etched on the back of card or to keep front simple you can put all detail on back of card, I will leave the lay out to you.

Colours in logo are

Pantone 144 C Orange
Pantone 11-0601 White
Pantone 7539 C Gray
Pantone 426 C Black

However black will be the base of black metal card. Gray will be replaced with the etching in card revealing the silver. Orange and white will be printed on card.

Please have fun!!
Should not have
• Please don't clutter the card
No fonts smaller then 7 points

```html
<!DOCTYPE html>
<html lang="en">
<head>
<meta charset="utf-8">
<title>Norwick Vale Construction – Business Card</title>
<link rel="stylesheet" href="https://fonts.googleapis.com/css2?family=Saira:wght@400;500;600&display=swap">
<style>
  :root {
    --backdrop: #1b1b1b;
    --card-black: #000000;
    --card-edge: #5a5a57;
    --orange: #f26522;
    --white: #f4f4f1;
    --steel: #a7a9ac;
  }
  * { margin: 0; padding: 0; box-sizing: border-box; }
  html, body {
    width: 1200px;
    height: 801px;
    overflow: hidden;
    background: var(--backdrop);
    font-family: "Saira", "Arial", sans-serif;
  }
  .canvas {
    position: relative;
    width: 1200px;
    height: 801px;
  }
  .card {
    position: absolute;
    width: 544px;
    height: 311px;
    background: var(--card-black);
    border: 1px solid var(--card-edge);
  }
  .card--front { left: 234px; top: 80px; }
  .card--back  { left: 423px; top: 410px; }

  /* Front */
  .brand {
    position: absolute;
    left: 66px;
    top: 80px;
    display: flex;
    align-items: center;
    gap: 16px;
  }
  .brand__mark {
    width: 26px;
    height: 26px;
    background: var(--orange);
  }
  .brand__name {
    color: var(--orange);
    font-weight: 600;
    font-size: 27px;
    letter-spacing: 1px;
    text-transform: uppercase;
    line-height: 1;
  }
  .brand__rule {
    position: absolute;
    left: 108px;
    top: 136px;
    width: 368px;
    height: 2px;
    background: var(--steel);
  }
  .tagline {
    position: absolute;
    left: 0;
    right: 0;
    top: 259px;
    text-align: center;
    color: var(--orange);
    font-size: 15px;
    font-weight: 400;
    letter-spacing: 0.2px;
  }

  /* Back */
  .person {
    position: absolute;
    left: 56px;
    top: 128px;
  }
  .person__name {
    color: var(--orange);
    font-size: 16px;
    font-weight: 400;
    letter-spacing: 0.6px;
    line-height: 20px;
  }
  .person__role {
    color: var(--white);
    font-size: 14px;
    line-height: 18px;
  }
  .contact {
    position: absolute;
    left: 160px;
    top: 254px;
    display: flex;
    align-items: center;
    color: var(--orange);
    font-size: 15px;
  }
  .contact__item {
    display: flex;
    align-items: center;
  }
  .contact__item + .contact__item { margin-left: 20px; }
  .contact__item::before {
    content: "";
    display: inline-block;
    width: 2px;
    height: 22px;
    background: var(--white);
    margin-right: 20px;
  }
</style>
</head>
<body>
<main class="canvas">
  <section class="card card--front" aria-label="Card front">
    <div class="brand">
      <span class="brand__mark" aria-hidden="true"></span>
      <span class="brand__name">Norwick Vale Construction</span>
    </div>
    <span class="brand__rule" aria-hidden="true"></span>
    <p class="tagline">COMMERCIAL PAINTING AND ROOFING</p>
  </section>

  <section class="card card--back" aria-label="Card back">
    <div class="person">
      <p class="person__name">LIAM CARTER</p>
      <p class="person__role">Director</p>
    </div>
    <div class="contact">
      <span class="contact__item">liam.c@norwickvale.com</span>
      <span class="contact__item">020 7946 0182</span>
    </div>
  </section>
</main>
</body>
</html>
```